Window cover film/full size advertisement.

Our company specializes in custom woodworking and cabinetry. We produce high end, custom build units for kitchens, bars, bathroom vanities, TV units, etc... Looking to have a design made to be printed on a perforated film to be placed on our office windows. The window placement and sizes can be found in the file attached. The best design must have pictures and logo as well as clearly visible phone number and website address. We are looking to cover 6 windows in the frond ( under the sigh) and 6 windows on the side of the building.

Tv

• should not have a lot of empty/white space on the design.

```html
<!DOCTYPE html>
<html lang="en">
<head>
<meta charset="utf-8">
<title>BrightNook Interiors – Window Film</title>
<link rel="stylesheet" href="https://fonts.googleapis.com/css2?family=Open+Sans:wght@600;700&family=Oswald:wght@600;700&display=swap">
<style>
  :root {
    --green-light: #a3d393;
    --green-mid: #6cb664;
    --green-deep: #51a64e;
    --blue-light: #5b80c2;
    --blue: #5679bd;
    --blue-deep: #4a6cb3;
    --blue-text: #a8b9e8;
    --brand-blue: #2f5ca8;
    --brand-green: #6abf4b;
    --white: #ffffff;
  }
  html, body {
    margin: 0;
    padding: 0;
    width: 1173px;
    height: 1200px;
    overflow: hidden;
    background: var(--white);
  }
  .window-film {
    display: block;
    width: 1173px;
    height: 1200px;
  }
  .tagline {
    font-family: "Open Sans", Arial, sans-serif;
    font-weight: 600;
    font-size: 60px;
    fill: var(--blue-text);
  }
  .brand-name {
    font-family: "Open Sans", Arial, sans-serif;
    font-weight: 700;
    font-size: 30px;
    fill: var(--brand-blue);
  }
  .website {
    font-family: "Open Sans", Arial, sans-serif;
    font-weight: 700;
    font-size: 22px;
    fill: var(--white);
  }
  .phone-label {
    font-family: "Oswald", "Arial Narrow", sans-serif;
    font-weight: 700;
    font-size: 56px;
    fill: var(--white);
  }
  .phone-number {
    font-family: "Oswald", "Arial Narrow", sans-serif;
    font-weight: 700;
    font-size: 100px;
    fill: var(--white);
  }
  .contact-line {
    font-family: "Open Sans", Arial, sans-serif;
    font-weight: 600;
    font-size: 26px;
    fill: var(--white);
  }
</style>
</head>
<body>
<svg class="window-film" viewBox="0 0 1203 1232" preserveAspectRatio="none" xmlns="http://www.w3.org/2000/svg">
  <defs>
    <linearGradient id="green-fill" x1="0" y1="0" x2="1" y2="1">
      <stop offset="0" stop-color="var(--green-light)"/>
      <stop offset="0.5" stop-color="var(--green-mid)"/>
      <stop offset="1" stop-color="var(--green-deep)"/>
    </linearGradient>
    <linearGradient id="blue-fill" x1="0" y1="0" x2="1" y2="1">
      <stop offset="0" stop-color="var(--blue-light)"/>
      <stop offset="0.5" stop-color="var(--blue)"/>
      <stop offset="1" stop-color="var(--blue-deep)"/>
    </linearGradient>
    <path id="tagline-path" d="M516,230 L1062,1150"/>
  </defs>

  <!-- green field -->
  <polygon class="green-field" fill="url(#green-fill)" points="0,0 300,0 995,1232 0,1232"/>

  <!-- blue field -->
  <polygon class="blue-field" fill="url(#blue-fill)" points="390,0 1203,0 1203,1232 1120,1232"
           role="img" aria-label="Blue decorative panel area"/>

  <!-- logo panel -->
  <rect class="logo-panel" x="805" y="0" width="398" height="214" fill="var(--white)"/>

  <!-- window mullions -->
  <g class="mullions" fill="var(--white)">
    <rect x="398" y="0" width="8" height="1232"/>
    <rect x="800" y="0" width="8" height="1232"/>
    <rect x="0" y="210" width="805" height="7"/>
  </g>

  <!-- diagonal tagline -->
  <text class="tagline">
    <textPath href="#tagline-path" textLength="1040" lengthAdjust="spacingAndGlyphs">custom woodworking and cabinetry</textPath>
  </text>

  <!-- brand -->
  <g class="brand">
    <rect x="970" y="34" width="62" height="62" fill="var(--brand-green)"/>
    <text class="brand-name" x="1001" y="170" text-anchor="middle">BrightNook Interiors</text>
  </g>

  <text class="website" x="833" y="255" textLength="347" lengthAdjust="spacingAndGlyphs">www.brightnookinteriors.ca</text>

  <!-- contact -->
  <g class="contact">
    <text class="phone-label" x="28" y="1003" textLength="148" lengthAdjust="spacingAndGlyphs">Phone:</text>
    <text class="phone-number" x="26" y="1107" textLength="586" lengthAdjust="spacingAndGlyphs">1-403-555-0142</text>
    <text class="contact-line" x="30" y="1165" textLength="125" lengthAdjust="spacingAndGlyphs">Toll-Free:</text>
    <text class="contact-line" x="30" y="1197" textLength="210" lengthAdjust="spacingAndGlyphs">1-844-555-0142</text>
    <text class="contact-line" x="434" y="1165" textLength="54" lengthAdjust="spacingAndGlyphs">Fax:</text>
    <text class="contact-line" x="434" y="1197" textLength="211" lengthAdjust="spacingAndGlyphs">1-403-555-0187</text>
  </g>
</svg>
</body>
</html>
```